Surveillance Sign

Design sign and stickers with a line drawing of the camera.

Industry/Entity Type

Camera

Requirements
• I like this design: http://www.brevondo.com/cctv-camera-warning-signs-decals/camera-surveillance-sign

```html
<!DOCTYPE html>
<html lang="en">
<head>
<meta charset="utf-8">
<title>Surveillance Sign</title>
<link rel="stylesheet" href="https://fonts.googleapis.com/css2?family=Anton&family=Roboto+Condensed:wght@700&family=Arimo:wght@700&display=swap">
<style>
  :root {
    --sign-red: #e61e26;
    --sign-yellow: #fde51a;
    --sign-black: #111111;
    --sign-white: #ffffff;
    --page-bg: #ffffff;
    --camera-light: #e9e9e9;
    --camera-dark: #9a9a9a;
  }
  * { margin: 0; padding: 0; box-sizing: border-box; }
  html, body {
    width: 1200px;
    height: 1183px;
    overflow: hidden;
    background: var(--page-bg);
  }
  .canvas {
    position: relative;
    width: 1200px;
    height: 1183px;
  }
  .sign {
    position: absolute;
    left: 9px;
    top: 9px;
    width: 1180px;
    height: 1164px;
    background: var(--sign-red);
    border: 7px solid var(--sign-black);
    border-radius: 42px;
    overflow: hidden;
  }
  .title-plate {
    position: absolute;
    left: 93px;
    top: 52px;
    width: 1005px;
    height: 199px;
    background: var(--sign-yellow);
    border: 7px solid var(--sign-black);
    border-radius: 28px;
    display: flex;
    align-items: center;
    justify-content: center;
  }
  .title {
    font-family: "Anton", "Oswald", sans-serif;
    font-size: 150px;
    line-height: 1;
    color: var(--sign-black);
    letter-spacing: 1px;
    transform: scaleX(0.98);
  }
  .info-band {
    position: absolute;
    left: 0;
    top: 281px;
    width: 100%;
    height: 584px;
    background: var(--sign-white);
  }
  .camera-art {
    position: absolute;
    left: 30px;
    top: 40px;
    width: 690px;
    height: 505px;
    border-radius: 24px;
    background: radial-gradient(ellipse at 55% 50%, var(--camera-light) 0%, #d2d2d2 60%, var(--camera-dark) 100%);
  }
  .protection-note {
    position: absolute;
    left: 730px;
    top: 48px;
    width: 420px;
    text-align: center;
    font-family: "Roboto Condensed", "Arial Narrow", sans-serif;
    font-weight: 700;
    font-size: 67px;
    line-height: 76px;
    color: var(--sign-black);
  }
  .notice {
    position: absolute;
    left: 68px;
    top: 885px;
    width: 1030px;
    font-family: "Arimo", "Arial", sans-serif;
    font-weight: 700;
    font-size: 40px;
    line-height: 61px;
    color: var(--sign-white);
  }
  .notice-line {
    display: block;
    text-align: justify;
    text-align-last: justify;
    letter-spacing: 2px;
    word-spacing: 4px;
  }
</style>
</head>
<body>
  <div class="canvas">
    <div class="sign">
      <div class="title-plate">
        <h1 class="title">SURVEILLANCE</h1>
      </div>
      <div class="info-band">
        <div class="camera-art" role="img" aria-label="Line drawing of a wall-mounted CCTV bullet camera with infrared LED ring"></div>
        <p class="protection-note">THIS<br>PROPERTY<br>PROTECTED<br>BY CCTV<br>SECURITY<br>CAMERAS</p>
      </div>
      <p class="notice">
        <span class="notice-line">FOR YOUR PERSONAL PROTECTION ALL</span>
        <span class="notice-line">ACTIVITIES ARE RECORDED ON DIGITAL</span>
        <span class="notice-line">MEDIA TO AID IN THE PROSECUTION OF ANY</span>
        <span class="notice-line">CRIME COMMITTED ON THIS PROPERTY</span>
      </p>
    </div>
  </div>
</body>
</html>
```